A private psychotherapy practice for seniors located on the upper west side of manhattan needs a pos

**Hi, Please note deadline was decreased by two days**

I am a Psychotherapist (LCSW) who has a Private Practice located on the Upper West Side of Manhattan. I accept Vitalcare and most other insurances. I treat Seniors who have health or financial issues, loss of spouse, feel sad most days, withdraw from social activities or have problems sleeping or eating. Psychotherapy allows individuals to relieve their feelings of sadness and to enjoy life again. I am a licensed clinical social worker with over fifteen years of experience and advanced training from Calderwood Analytic Academy.

Target Market(s)

Senior Citizens (65+) living on the upper west side of manhattan

Font styles to use
Serif

Requirements
Must have
• Broad appeal - diversified ethnic group if photos are used. Clear call to help those struggling with aging issues - especially living in New York City
Nice to have
• Hopeful and improved quality of life as result of psychotherapy treatment. Improved relations with family and friends.
Should not have
• Not depressing or too psycho bable.

```html
<!DOCTYPE html>
<html lang="en">
<head>
<meta charset="UTF-8">
<title>Vitalcare Postcard</title>
<link href="https://fonts.googleapis.com/css2?family=Tinos:wght@400;700&display=swap" rel="stylesheet">
<style>
  :root {
    --backdrop: #e9ecef;
    --card: #ffffff;
    --cyan: #3cc1e6;
    --cyan-light: #9fe0f3;
    --navy: #14213d;
    --label: #1b5e8c;
    --ink: #1f2a33;
    --rule: #9aa7b1;
  }
  * { box-sizing: border-box; margin: 0; padding: 0; }
  html, body { width: 900px; height: 1200px; overflow: hidden; }
  body {
    background: var(--backdrop);
    font-family: "Tinos", "Times New Roman", serif;
    color: var(--ink);
    position: relative;
  }
  .postcard {
    position: absolute;
    left: 50px;
    width: 800px;
    height: 540px;
    background: var(--card);
    box-shadow: 0 4px 14px rgba(0,0,0,0.18);
    overflow: hidden;
  }
  .postcard--front { top: 40px; }
  .postcard--back { top: 620px; }
  .postcard__art { position: absolute; inset: 0; width: 800px; height: 540px; }

  .front__domain {
    position: absolute; top: 14px; right: 22px;
    font-size: 12px; color: var(--navy);
  }
  .front__title {
    position: absolute; top: 70px; left: 500px; width: 280px;
    font-size: 40px; font-weight: 700; line-height: 1.15;
    color: var(--navy); text-align: center;
  }
  .section-label {
    position: absolute;
    background: var(--label);
    color: #fff;
    font-size: 22px; font-weight: 700;
    padding: 3px 14px;
    border: 2px solid #fff;
  }
  .front__label { top: 358px; left: 18px; }
  .front__about {
    position: absolute; top: 402px; left: 22px; width: 430px;
    font-size: 16.5px; line-height: 1.3; color: #fff;
  }
  .back__label { top: 22px; left: 40px; width: 190px; font-style: italic; }
  .back__service {
    position: absolute; top: 68px; left: 40px; width: 390px;
    font-size: 16.5px; line-height: 1.3; color: var(--ink);
  }
  .back__stamp {
    position: absolute; top: 30px; right: 36px;
    width: 90px; height: 104px;
    border: 2px dashed var(--rule);
  }
  .back__address {
    position: absolute; left: 520px; width: 240px;
    height: 0; border-top: 1.5px solid var(--rule);
  }
</style>
</head>
<body>

<section class="postcard postcard--front">
  <svg class="postcard__art" viewBox="0 0 800 540" aria-hidden="false">
    <defs>
      <linearGradient id="couplePhoto" x1="0" y1="0" x2="1" y2="1">
        <stop offset="0" stop-color="#c9d3cf"/>
        <stop offset="0.5" stop-color="#e4c6ae"/>
        <stop offset="1" stop-color="#b7c6c0"/>
      </linearGradient>
      <linearGradient id="manPhoto" x1="0" y1="0" x2="1" y2="1">
        <stop offset="0" stop-color="#3a3f44"/>
        <stop offset="0.6" stop-color="#5a5450"/>
        <stop offset="1" stop-color="#1e2226"/>
      </linearGradient>
    </defs>
    <path class="band" d="M0 330 C180 300 320 360 480 330 C620 305 720 250 800 230 L800 540 L0 540 Z" fill="var(--cyan)"/>
    <path d="M0 0 H470 C490 120 400 240 300 285 C200 330 90 320 0 350 Z" fill="var(--cyan-light)"/>
    <path role="img" aria-label="Photo of a smiling senior couple" d="M0 0 H450 C465 115 385 225 290 268 C195 310 85 305 0 332 Z" fill="url(#couplePhoto)"/>
    <path role="img" aria-label="Photo of a pensive senior man" d="M800 250 L800 520 L480 520 C490 390 600 275 800 250 Z" fill="url(#manPhoto)"/>
    <path d="M800 240 C600 268 482 385 470 520" fill="none" stroke="#fff" stroke-width="8"/>
    <rect x="0" y="520" width="800" height="20" fill="#fff"/>
  </svg>
  <p class="front__domain">www.yourwebsite.com</p>
  <h1 class="front__title">Your Vitalcare center name</h1>
  <h2 class="section-label front__label">About Myself:</h2>
  <p class="front__about">I am a Psychotherapist (LCSW) who has a Private Practice located on the Upper West Side of Manhattan I am a licensed clinical social worker with over fifteen years of experience and advanced training from Calderwood Analytic Academy.</p>
</section>

<section class="postcard postcard--back">
  <svg class="postcard__art" viewBox="0 0 800 540">
    <defs>
      <linearGradient id="restPhoto" x1="0" y1="0" x2="1" y2="1">
        <stop offset="0" stop-color="#3b2f2c"/>
        <stop offset="0.5" stop-color="#a88874"/>
        <stop offset="1" stop-color="#e7e0dc"/>
      </linearGradient>
    </defs>
    <rect x="0" y="20" width="30" height="250" fill="var(--cyan)"/>
    <path d="M0 280 C140 300 300 300 460 350 L460 520 L0 520 Z" fill="var(--cyan)"/>
    <path role="img" aria-label="Photo of a woman resting in bed" d="M0 305 C140 318 280 320 430 368 L430 505 L0 505 Z" fill="url(#restPhoto)"/>
    <line x1="470" y1="30" x2="470" y2="505" stroke="var(--cyan-light)" stroke-width="2"/>
  </svg>
  <h2 class="section-label back__label">our service:</h2>
  <p class="back__service">I accept Vitalcare and most other insurances. I treat Seniors who have health or financial issues, loss of spouse, feel sad most days, withdraw from social activities or have problems sleeping or eating. Psychotherapy allows individuals to relieve their feelings of sadness and to enjoy life again.</p>
  <div class="back__stamp"></div>
  <div class="back__address" style="top:290px"></div>
  <div class="back__address" style="top:330px"></div>
  <div class="back__address" style="top:370px"></div>
</section>

</body>
</html>
```